Mexican Restaurant - Flyer for takeaway and delivery customers

We are a Mexican Restaurant.  We need a flyer for home delivery customers...should include our menu, photos, prices and location etc....
I have attached our menu, logo and some photos...feel free to use some of your own.  Please ask if you have any questions.
we prefer a one page (front and back) A4 or A5 size.  If that is not possible because of the number of items, maybe a booklet type flyer is acceptable.
WE also need the following text:
Salsa Verde Cantina - New in MKQB!
Unit R7-23
Level R7
Lumen Spires
Meridian Quarter Kalvar Bourse
The phone number of :  04 385 1962
And the verbiage "Free Parking Available"!
Please reference the colors on the examples provided
If you can use Minion Pro font that would be great

```html
<!DOCTYPE html>
<html lang="en">
<head>
<meta charset="utf-8">
<title>Salsa Verde Cantina – Flyer</title>
<link href="https://fonts.googleapis.com/css2?family=Crimson+Pro:wght@400;600;700&display=swap" rel="stylesheet">
<style>
  :root{
    --sky:#c1e9f7;
    --ink:#121212;
    --ink-soft:#1c1c1c;
    --red:#e8334a;
    --red-dark:#b52636;
    --blue:#27b9e6;
    --white:#ffffff;
  }
  *{margin:0;padding:0;box-sizing:border-box}
  html,body{width:1200px;height:1200px;overflow:hidden;background:var(--sky)}
  body{position:relative;font-family:"Crimson Pro",Georgia,serif;color:var(--white)}

  .page{position:absolute;top:199px;width:520px;height:735px;overflow:hidden;
    background:linear-gradient(90deg,var(--ink) 0%,var(--ink-soft) 50%,var(--ink) 100%)}
  .page--front{left:71px}
  .page--menu{left:627px}
  .page svg.art{position:absolute;inset:0;width:520px;height:735px}

  /* front */
  .brand{position:absolute;left:152px;top:134px;width:218px;text-align:center}
  .brand__name{font-size:23px;font-weight:600;color:var(--red);line-height:1.1;margin-top:78px}
  .brand__tag{font-size:8.5px;letter-spacing:.9px;color:var(--blue);margin-top:10px}
  .headline{position:absolute;left:0;width:520px;top:388px;text-align:center;font-size:27px;font-weight:400;letter-spacing:.3px;color:var(--red)}
  .headline span{color:var(--blue)}
  .address{position:absolute;left:0;width:520px;top:427px;text-align:center;font-size:17px;line-height:21px}
  .call{position:absolute;background:var(--blue);color:var(--ink);font-weight:700;border-radius:4px;text-align:center;white-space:nowrap}
  .call--front{left:76px;top:560px;width:367px;height:33px;font-size:26px;line-height:33px;letter-spacing:.4px}
  .parking{position:absolute;left:0;width:520px;text-align:center;font-weight:700;letter-spacing:.4px}
  .parking--front{top:602px;font-size:20px}

  /* menu */
  .menu-col{position:absolute;font-size:8.6px;line-height:10.6px}
  .menu-col--left{left:40px;width:214px}
  .menu-col--right{left:276px;width:212px}
  .menu-section{position:absolute;left:0;width:100%}
  .menu-section h2{font-size:12.5px;font-weight:400;color:var(--red);letter-spacing:.3px;line-height:14px;margin-bottom:6px}
  .item{margin-bottom:10px}
  .item__name{color:var(--blue)}
  .price{background:var(--blue);color:var(--ink);font-size:6.8px;padding:0 3px;white-space:nowrap}
  .call--menu{left:120px;top:673px;width:281px;height:26px;font-size:21px;line-height:26px}
  .parking--menu{top:702px;font-size:19px}
</style>
</head>
<body>

<section class="page page--front">
  <svg class="art" viewBox="0 0 520 735" aria-hidden="false">
    <g>
      <polygon role="img" aria-label="Photo: chicken tortilla with diced tomato, onion and coriander" points="0,0 150,0 205,177 0,177" fill="#c9a385"/>
      <polygon role="img" aria-label="Photo: plate of chicken tacos on a red platter" points="157,0 405,0 356,177 212,177" fill="#b5402f"/>
      <polygon role="img" aria-label="Photo: guacamole with tortilla chips" points="412,0 520,0 520,177 363,177" fill="#7a6a3e"/>
      <rect role="img" aria-label="Photo: crispy rolled tacos with lettuce" x="0" y="183" width="190" height="137" fill="#b9b27a"/>
      <rect role="img" aria-label="Photo: rolled flour tortillas on a blue plate" x="340" y="183" width="180" height="137" fill="#7fa9b3"/>
      <rect role="img" aria-label="Photo: burrito cut in half" x="0" y="639" width="255" height="96" fill="#a89580"/>
      <rect role="img" aria-label="Photo: tacos on a red platter with salsa" x="261" y="639" width="259" height="96" fill="#c25a36"/>
    </g>
    <circle cx="261" cy="243" r="110" fill="#141414"/>
    <path d="M0 330 H162 C190 366 225 373 261 373 C297 373 332 366 360 330 H520" fill="none" stroke="var(--red)" stroke-width="4"/>
    <path d="M170 560 C185 520 225 496 271 496 C317 496 357 520 372 560 Z" fill="var(--blue)"/>
    <path d="M0 556 H156 C175 510 220 487 271 487 C322 487 367 510 386 556 H520" fill="none" stroke="var(--red)" stroke-width="4"/>
  </svg>

  <div class="brand">
    <div class="brand__name">Salsa Verde Cantina</div>
    <div class="brand__tag">AUTHENTIC MEXICAN FOOD</div>
  </div>

  <h1 class="headline">SALSA VERDE CANTINA- <span>NEW IN MKQB!</span></h1>
  <p class="address">Unit R7-23, Level R7, Lumen Spires<br>Meridian Quarter Kalvar Bourse</p>
  <div class="call call--front">CALL US NOW&nbsp; 04 385 1962</div>
  <p class="parking parking--front">FREE PARKING AVAILABLE</p>
</section>

<section class="page page--menu">
  <svg class="art" viewBox="0 0 520 735">
    <path d="M0 0 H520 V14 L508 17 L497 12 L486 19 L472 14 L458 21 L444 15 L430 18 L418 13 L404 20 L390 14 L376 17 L362 12 L348 19 L334 15 L320 21 L306 14 L292 18 L278 13 L264 19 L250 14 L236 20 L222 15 L208 18 L194 12 L180 19 L166 14 L152 21 L138 15 L124 18 L110 13 L96 20 L82 14 L68 18 L54 12 L40 19 L26 15 L12 20 L0 15 Z" fill="var(--red-dark)"/>
    <rect x="0" y="688" width="520" height="47" fill="var(--red)"/>
    <path d="M212 680 C220 662 240 653 258 653 C276 653 296 662 304 680 Z" fill="var(--blue)"/>
  </svg>

  <div class="menu-col menu-col--left">
    <div class="menu-section" style="top:49px">
      <h2>APPETIZERS</h2>
      <div class="item"><span class="item__name">Guacamole</span><br><br>Served with our home-made corn tortilla chips (250g) <span class="price">AED 42.00</span></div>
      <div class="item"><span class="item__name">Salsa Verde Cantina Nachos -Traditional (no meat):</span><br>Traditional (no meat): <span class="price">AED 32.00</span> With either pastor (marinated steak ), steak or chicken:<br><br><span class="price">AED 44.00</span></div>
      <div class="item" style="margin-top:16px"><span class="item__name">Tacos dorados</span><br>Served with fresh lettuce, tomato, cream and cheese <span class="price">AED 19.00</span></div>
      <div class="item" style="margin-top:16px"><span class="item__name">Quesadilla</span><br>with melted cheese served with cream and a dab of guacamole. <span class="price">AED 20.00</span> Mushrooms <span class="price">AED 25.00</span> Pastor (marinated steak), steak or chicken <span class="price">AED 30.00</span></div>
    </div>

    <div class="menu-section" style="top:296px">
      <h2>FROM THE GRILL</h2>
      <div class="item"><span class="item__name">Sope</span> Served with refried beans, lettuce, cream, and velvety cheese. <span class="price">AED 27.00</span></div>
      <div class="item"><span class="item__name">Huarache</span> Slightly thicker corn tortilla served with refried beans, cheese, lettuce, avocado, green or red salsa and the meat of your choice: -Pastor (marinated steak), steak or chicken. <span class="price">AED 39.00</span></div>
      <div class="item"><span class="item__name">Tinga quesadilla</span> Corn tortila served with freshly seasoned pulled chicken that has been marinated in a fresh tomato base served with refried beans, cheese, onion, coriander, and fresh tomato. <span class="price">AED 44.00</span> -With mushrooms.-Add extra cheese. <span class="price">AED 47.00</span></div>
      <div class="item"><span class="item__name">Volcan</span> Three crispy corn tortillas served with melted cheese and steak. <span class="price">AED 48.00</span></div>
    </div>

    <div class="menu-section" style="top:510px">
      <h2>MAKE YOUR<br>OWN BURRITO!</h2>
      <div class="item">Base includes: lettuce, refried beans or black beans, cream and cheese.<br>Normal size: <span class="price">AED 16.00</span><br>Mega size: &nbsp;&nbsp;&nbsp;&nbsp;<span class="price">AED 21.00</span><br>Your choice of meat (150g).<br>Pastor (marinated steak)<br>-Steak -Chicken <span class="price">AED +10.00</span></div>
    </div>
  </div>

  <div class="menu-col menu-col--right">
    <div class="menu-section" style="top:49px">
      <h2>TACOS</h2>
      <div class="item"><span class="item__name">Ketaco</span> A hard taco shell that is made with cheese! Filled with your favorite pastor (marinated steak), steak or chicken. <span class="price">AED 37.00</span></div>
      <div class="item"><span class="item__name">Gringa</span> Three flour tortillas with pastor (marinated steak) grilled in flavorful cheese, coriander, onion and pineapple! <span class="price">AED 37.00</span></div>
      <div class="item"><span class="item__name">Tacos al pastor</span> Marinated steak <span class="price">AED 30.00</span> Corn tortilla (order of 3) Flour tortilla (order of 2) -Add cheese <span class="price">AED +5.00</span></div>
      <div class="item"><span class="item__name">Mula terca</span> Three flour tortillas with steak, beef bacon and melted cheese. <span class="price">AED 40.00</span></div>
      <div class="item"><span class="item__name">Hawaiana</span> The house secret, chicken, turkey breast ham, pineapple, beef bacon and cheese all inside three flour tortillas. <span class="price">AED 40.00</span></div>
      <div class="item"><span class="item__name">Chicken or steak Tacos.</span> <span class="price">AED 30.00</span><br>Corn tortilla (order of 3) Flour tortilla (order of 2) Cheese tortilla (order of 1) -Add Cheese <span class="price">AED +5.00</span></div>
      <div class="item"><span class="item__name">Veggie.</span> <span class="price">AED 30.00</span><br>Corn tortilla (order of 3) Flour tortilla (order of 2) Cheese tortilla (order of 1) -Add cheese <span class="price">AED +5.00</span></div>
    </div>

    <div class="menu-section" style="top:366px">
      <h2>ALAMBRES</h2>
      <div class="item"><span class="item__name">Alambre tradicional</span> Beef bacon, bell peppers , onion, melted cheese with your choice of meat: pastor (marinatedsteak), steak or chicken. <span class="price">AED 50.00</span></div>
      <div class="item"><span class="item__name">Alambre de barrio</span> All of your favorites from the Alambre tradicional but with a mix of pastor (marinated steak) and steak. <span class="price">AED 55.00</span></div>
      <div class="item"><span class="item__name">Vegatarian alambre</span> Onion, bell peppers, mushrooms and cheese. <span class="price">AED 47.00</span></div>
    </div>

    <div class="menu-section" style="top:505px">
      <h2>DESERTS</h2>
      <div class="item"><span class="item__name">Arroz con leche</span> Mexico's rice pudding , with a touch of cinnamon for make it more delicious. <span class="price">AED 10.00</span></div>
      <div class="item"><span class="item__name">Flan</span> Custard base dessert with a flavorful caramel on top. <span class="price">AED 10.00</span></div>
      <div class="item"><span class="item__name">Fruit chamoy</span> All areas of your taste buds will be affected by this truly Mexican's avory sauce. A salty, sweet, sour and a mild spice sauce drizzled over fresh fruit. <span class="price">AED 15.00</span></div>
    </div>
  </div>

  <div class="call call--menu">CALL US NOW&nbsp; 04 385 1962</div>
  <p class="parking parking--menu">FREE PARKING AVAILABLE</p>
</section>

</body>
</html>
```